Agricultural Consulting Website

Provide a modern yet business like website for my new Agriculture Consulting Business in Australia called FieldNorth. Whilst we are based in Australia we are targetting both domestic and international markets (especially in Asia). We are targetting corporate, small business, government and farmer clients. The design should compliment our logo also sourced through pixel harbor. The webiste should be easy for me to keep updated on a regular basis without the need to go back to the designer.

Industry/Entity Type

Business

Requirements
Must have
• clean crisp feel
• be modern yet business like
• be able to be updated by myself easily

```html
<!DOCTYPE html>
<html lang="en">
<head>
<meta charset="utf-8">
<title>FieldNorth – Agricultural Consulting</title>
<link href="https://fonts.googleapis.com/css2?family=Lato:ital,wght@0,300;0,400;0,700;1,400&display=swap" rel="stylesheet">
<style>
:root{
  --green:#5b9a2c;
  --green-dark:#4a8420;
  --brown:#6a3510;
  --brown-soft:#8a5a34;
  --ink:#333;
  --ink-soft:#555;
  --muted:#888;
  --rule:#ddd;
  --page:#ececec;
  --white:#fff;
  --footer:#2a2a2a;
  --footer-base:#1f1f1f;
  --footer-text:#8c8c8c;
}
*{box-sizing:border-box;margin:0;padding:0}
html,body{width:1200px;height:2175px;overflow:hidden}
body{background:var(--page);font-family:"Lato",sans-serif;color:var(--ink);position:relative}
.abs{position:absolute}
h2,h3,h4{font-weight:300}
.accent{color:var(--green)}
.btn{display:inline-block;background:var(--green);color:var(--white);font-size:11px;text-align:center;border:1px solid var(--green-dark)}
.btn-light{background:var(--white);color:var(--ink);border:1px solid #ccc}

/* top bar */
.topbar{top:10px;left:830px;display:flex;align-items:center;gap:10px}
.topbar .dot{width:11px;height:11px;border-radius:50%;background:#999}
.search{width:155px;height:20px;background:var(--white);border:1px solid #ccc;margin-left:6px;position:relative}
.search svg{position:absolute;right:5px;top:4px}

.sheet{top:36px;left:78px;width:1045px;height:1604px;background:var(--white);border-top:2px solid var(--green)}

/* header */
.brand{top:70px;left:110px;display:flex;align-items:center;gap:10px}
.brand .mark{width:68px;height:68px;background:var(--brown)}
.brand .name{font-size:40px;color:var(--green);font-weight:400}
.nav{top:88px;right:95px;display:flex;gap:30px;font-size:17px}
.nav a{color:var(--green);text-decoration:none}
.nav a.current{color:var(--ink)}

/* hero */
.hero{top:181px;left:78px;width:1045px;height:402px;background:linear-gradient(180deg,#a9cbe8 0%,#d8e6ef 22%,#c9b870 34%,#8fae3a 48%,#4f8f22 70%,#3d7a1a 100%)}
.hero .veil{position:absolute;left:0;top:0;width:402px;height:100%;background:rgba(255,255,255,.38)}
.tag{position:absolute;white-space:nowrap}
.tag-lg{left:27px;font-size:26px;padding:2px 12px;font-weight:300}
.tag-lg.light{top:69px;background:var(--white);color:var(--ink)}
.tag-lg.solid{top:108px;background:var(--green);color:var(--white)}
.tag-sm{left:27px;font-size:16px;font-weight:300;padding:2px 12px;background:var(--brown);color:var(--white)}
.tag-sm.one{top:279px;width:221px}
.tag-sm.two{top:307px;width:265px}

/* about */
.about-title{top:605px;left:96px;font-size:31px}
.about-text{top:660px;left:96px;width:760px;font-size:10px;line-height:17px;color:var(--ink-soft)}
.contact-box{top:583px;left:883px;width:240px;height:159px;background:var(--brown);color:var(--white);padding:12px 16px}
.contact-box .call{font-size:22px;font-weight:300}
.contact-box .fax{font-size:17px;font-weight:300;margin-top:4px}
.contact-box .mail{font-size:10px;margin-top:10px}
.contact-box .circles{display:flex;gap:10px;margin-top:14px}
.contact-box .circles span{width:33px;height:33px;border-radius:50%;background:var(--brown-soft)}
.rule-full{left:78px;width:1045px;height:1px;background:#e4e4e4}

/* services */
.service{top:770px;width:225px}
.service h3{font-size:21px}
.service .row{display:flex;gap:12px;margin-top:14px}
.service .icon{width:42px;height:42px;border-radius:50%;background:#d9d9d9;flex:none}
.service p{font-size:10.5px;line-height:18px;color:var(--ink-soft)}
.service .btn{position:absolute;right:0;top:115px;width:74px;height:28px;line-height:26px}
.service.wide .btn{width:222px}

/* posts */
.section-title{font-size:26px}
.posts-title{top:975px;left:100px}
.post{width:225px}
.thumb{background:linear-gradient(160deg,#8aa6c4,#7e9a52 55%,#b88a3a)}
.post .thumb{width:225px;height:135px}
.post h4{font-size:12.5px;font-weight:700;margin-top:14px}
.date{font-size:9.5px;font-style:italic;color:var(--muted);margin-top:10px}
.post p{font-size:10.5px;line-height:18px;color:var(--ink-soft);margin-top:14px}

.events-title{top:1357px;left:100px;width:740px;border-bottom:1px solid var(--rule);padding-bottom:8px}
.event{top:1423px;width:170px}
.event.last{width:135px}
.event .thumb{width:100%;height:126px}
.event h4{font-size:12.5px;font-weight:700;margin-top:14px;white-space:nowrap}
.carousel-next{position:absolute;right:4px;top:48px;width:30px;height:30px;border-radius:50%;background:rgba(40,40,40,.6)}

/* sidebar */
.side{left:880px;width:220px}
.side h3{font-size:20px;border-bottom:1px solid var(--rule);padding-bottom:8px}
.side .row{display:flex;gap:18px;margin-top:18px}
.side .avatar{width:38px;height:38px;background:#555;flex:none}
.side p{font-size:10.5px;line-height:19px;color:var(--ink-soft)}
.side .btn{position:absolute;right:0;width:73px;height:28px;line-height:26px}
.quote{font-size:11px;font-style:italic;line-height:18px;color:var(--ink-soft);padding-left:20px}

/* newsletter */
.newsletter{top:1642px;left:78px;width:1045px;height:102px;background:var(--green);border:2px solid #7bb54a;color:var(--white);padding:14px 20px}
.newsletter h3{font-size:22px}
.newsletter p{font-size:10.5px;line-height:17px;width:670px;margin-top:8px}
.newsletter .field{position:absolute;left:735px;top:40px;width:196px;height:27px;background:var(--white);color:var(--muted);font-size:12px;padding:5px 9px}
.newsletter .go{position:absolute;left:937px;top:40px;width:80px;height:27px;background:var(--white);color:var(--ink-soft);font-size:12px;text-align:center;line-height:27px}

/* footer */
.footer{top:1747px;left:78px;width:1045px;height:350px;background:var(--footer);color:var(--footer-text)}
.footer h3{position:absolute;font-size:16.5px;color:#bbb;border-bottom:1px solid #444;padding-bottom:10px}
.footer .about-copy{position:absolute;left:22px;top:72px;width:620px;font-size:10px;line-height:17px}
.footer .know{position:absolute;left:652px;top:91px;width:113px;height:38px;line-height:36px;font-size:14px}
.reach{position:absolute;left:809px;top:72px;font-size:10.5px;line-height:19px;width:215px}
.reach strong{color:#bbb}
.reach .link{color:var(--green)}
.reach .page-btn{display:inline-block;background:var(--white);color:var(--ink);font-size:10px;padding:4px 8px;margin-top:10px}
.grid{position:absolute;top:212px;display:grid;grid-template-columns:repeat(3,50px);gap:8px}
.grid span{height:50px;background:linear-gradient(150deg,#9a7a4a,#6b8a3a)}
.tweet{position:absolute;left:403px;top:212px;width:170px;font-size:10.5px;line-height:19px;padding-left:30px}
.links{position:absolute;left:595px;top:214px;display:grid;grid-template-columns:55px 60px;font-size:9.5px;line-height:19px}
.copyright{top:2097px;left:78px;width:1045px;height:43px;background:var(--footer-base);color:#888;font-size:10px;text-align:center;line-height:43px}
</style>
</head>
<body>

<div class="abs topbar" aria-label="Social links and search">
  <span class="dot"></span><span class="dot"></span><span class="dot"></span><span class="dot"></span><span class="dot"></span>
  <div class="search"><svg width="11" height="11" viewBox="0 0 11 11"><circle cx="4.5" cy="4.5" r="3.5" fill="none" stroke="#888" stroke-width="1.4"/><line x1="7" y1="7" x2="10" y2="10" stroke="#888" stroke-width="1.5"/></svg></div>
</div>

<div class="abs sheet"></div>

<header>
  <div class="abs brand"><span class="mark"></span><span class="name">FieldNorth</span></div>
  <nav class="abs nav">
    <a class="current">Home</a><a>About</a><a>Activities</a><a>Events</a><a>Members</a><a>Career</a><a>Contact</a>
  </nav>
</header>

<section class="abs hero" role="img" aria-label="Rows of green crops stretching to rolling hills under a blue sky">
  <div class="veil"></div>
  <div class="tag tag-lg light">Lorem Ipsum is simply</div>
  <div class="tag tag-lg solid">Dummy text of the printing</div>
  <div class="tag tag-sm one">Lorem Ipsum is simply</div>
  <div class="tag tag-sm two">Dummy text of the printing</div>
</section>

<h2 class="abs about-title">About Harvest Advisory <span class="accent">Group</span></h2>
<p class="abs about-text">Tons of shortcodes shortcodes. Lorem ipsum dolor sit amet, consectetuer adipiscing elit,sed diam nonummy nibh euismod tincidunt ut laoreet dolore magna aliquam erat volutpat. Ut wisi enim ad minim veniam, quis nostrud exerci tation ullamcorper suscipit lobortis nisl ut aliquip ex ea commodo consequat.d tincidunt ut laoreet dolore magna aliquam erat volutpat. Ut wisi enim ad minim vemodo consequat.</p>
<aside class="abs contact-box">
  <div class="call">Call: 1800-555-0142</div>
  <div class="fax">Fax: (230)-555-0193</div>
  <div class="mail">Want to E-mail us?</div>
  <div class="circles"><span></span><span></span><span></span><span></span><span></span></div>
</aside>
<div class="abs rule-full" style="top:742px"></div>

<section>
  <div class="abs service" style="left:100px">
    <h3>Farm <span class="accent">Schemes</span></h3>
    <div class="row"><span class="icon" role="img" aria-label="Wheat icon"></span><p>Lorem ipsum dolor sit amet, sum dolor sit amet, consectetuer adipiscing elit, sed diam...</p></div>
    <span class="btn">More Info</span>
  </div>
  <div class="abs service" style="left:360px">
    <h3>Farm <span class="accent">Safety</span></h3>
    <div class="row"><span class="icon" role="img" aria-label="Seedling in hand icon"></span><p>Lorem ipsum dolor sit amet, sum dolor sit amet, consectetuer adipiscing elit, sed diam...</p></div>
    <span class="btn">More Info</span>
  </div>
  <div class="abs service" style="left:620px">
    <h3>Training <span class="accent">Cources</span></h3>
    <div class="row"><span class="icon" role="img" aria-label="Garden tools icon"></span><p>Lorem ipsum dolor sit amet, sum dolor sit amet, consectetuer adipiscing elit, sed diam...</p></div>
    <span class="btn">Learn More</span>
  </div>
  <div class="abs service wide" style="left:880px">
    <h3>Cotton Industry <span class="accent">Surveys</span></h3>
    <div class="row"><span class="icon" role="img" aria-label="Cotton boll icon"></span><p>Lorem ipsum dolor sit amet, sum dolor sit amet, consectetuer adipiscing elit, sed diam...</p></div>
    <span class="btn">Learn More</span>
  </div>
</section>
<div class="abs rule-full" style="top:950px;left:100px;width:1000px"></div>

<h2 class="abs section-title posts-title">Recent <span class="accent">Posts</span></h2>
<article class="abs post" style="top:1035px;left:100px">
  <div class="thumb" role="img" aria-label="Combine harvester in a golden wheat field"></div>
  <h4>Lorem ipsum dolor sit amet</h4><div class="date">Nov 29th,2013</div>
  <p>Lorem ipsum dolor sit amet, consectetuer adipiscing elit, sed diam nonummy nibh euismod tincidunt ut laoreet dolore magna [...]</p>
</article>
<article class="abs post" style="top:1035px;left:358px">
  <div class="thumb" role="img" aria-label="Group of farm workers standing beside grain sacks"></div>
  <h4>Consectetuer adipiscing elit</h4><div class="date">Nov 29th,2013</div>
  <p>Lorem ipsum dolor sit amet, consectetuer adipiscing elit, sed diam nonummy nibh euismod tincidunt ut laoreet dolore magna [...]</p>
</article>
<article class="abs post" style="top:1035px;left:614px">
  <div class="thumb" role="img" aria-label="Cotton field in front of mountains under cloudy sky"></div>
  <h4>Typi non habent claritatem insitam</h4><div class="date">Nov 29th,2013</div>
  <p>Lorem ipsum dolor sit amet, consectetuer adipiscing elit, sed diam nonummy nibh euismod tincidunt ut laoreet dolore magna [...]</p>
</article>

<h2 class="abs section-title events-title">Latest <span class="accent">Events &amp; News</span></h2>
<article class="abs event" style="left:100px"><div class="thumb" role="img" aria-label="Delegates seated at a conference table"></div><h4>Lorem ipsum dolor sit amet</h4><div class="date">Nov 29th,2013</div></article>
<article class="abs event" style="left:302px"><div class="thumb" role="img" aria-label="Audience at a presentation seminar"></div><h4>Consectetuer adipiscing elit</h4><div class="date">Nov 29th,2013</div></article>
<article class="abs event" style="left:503px"><div class="thumb" role="img" aria-label="Tractor spraying between orchard rows"></div><h4>Typi non habent</h4><div class="date">Nov 29th,2013</div></article>
<article class="abs event last" style="left:703px"><div class="thumb" role="img" aria-label="Two farmers shaking hands in a field"></div>
  <span class="carousel-next"><svg width="30" height="30" viewBox="0 0 30 30"><path d="M12 9l6 6-6 6" fill="none" stroke="#fff" stroke-width="2.5"/></svg></span>
  <h4>Lorem Ipsum habent</h4><div class="date">Nov 29th,2013</div></article>

<aside>
  <div class="abs side" style="top:980px">
    <h3>Membership <span class="accent">Info</span></h3>
    <div class="row"><span class="avatar" role="img" aria-label="Member icon"></span><p>Harvest Advisory Group Incorporated has approximately 200 financial members, made up of</p></div>
    <span class="btn" style="top:125px">More Info</span>
  </div>
  <div class="abs side" style="top:1152px">
    <h3>Membership <span class="accent">Categories</span></h3>
    <div class="row"><span class="avatar" role="img" aria-label="Members group icon"></span><p>There are four membership categories in addition to special membership awards presented</p></div>
    <span class="btn btn-light" style="top:124px">More Info</span>
  </div>
  <div class="abs side" style="top:1325px">
    <h3>Client <span class="accent">Testimonial</span></h3>
    <p class="quote" style="margin-top:38px">"Aeadipiscint wisi enim ad minim venig elit,sed diam nonu mmy nibh euismod tdead ipiscint wisi enim inamini incminim vidunt ut laoreet dolore magna aliqua minim vm erat.."</p>
    <div class="row" style="margin-top:16px;align-items:center;gap:14px"><span class="avatar" style="width:24px;height:24px;background:#777" role="img" aria-label="Client icon"></span><strong style="font-size:10.5px">Jane Holloway,</strong></div>
  </div>
</aside>

<section class="abs newsletter">
  <h3>Subscribe to our Newsletter</h3>
  <p>Please subscribe for lates News and Updates. Lorem ipsum dolor sit amet, consectetuer adipiscing elit, sed diam nonummy nibh euismod tincidunt ut laoreet dolore magna aliquam erat volutpat.</p>
  <div class="field">Email</div>
  <div class="go">Subscribe</div>
</section>

<footer class="abs footer">
  <h3 style="left:22px;top:22px;width:688px">About FieldNorth.com</h3>
  <p class="about-copy">Lorem ipsum dolor sit amet, consectetuer adipiscing elit, sed diam nonummy nibh euismod tincidunt ut laoreet dolore magna aliquam erat volutpat. Ut wisi enim ad minim veniam, quis nostrud exerci tation ullamcorper suscipit lobortis nisl ut aliquip ex ea commodo consequat. Duis autem vel eum iriure dolor in hendrerit in vulputate velit esse molestie consequat, vel illum dolore eu feugiat nulla facilisis at ver</p>
  <span class="btn know">Know More</span>

  <h3 style="left:809px;top:22px;width:215px;border:none">Reach <span class="accent">Us</span></h3>
  <div class="reach">
    <strong>FieldNorth Company Inc.</strong><br>
    Lorem ipsum dolor sit amet, sum dolor sitamet, con-sectetuer adipiscing elit,<br>
    P: (123)555-0130<br>Fax: (422)555-0190<br>Map: Get Directions<br><br>
    Email: <span class="link">info@fieldnorth.example</span><br>
    Website: <span class="link">www.fieldnorth.example</span><br>
    <span class="page-btn">Contact Page</span>
  </div>

  <h3 style="left:22px;top:162px;width:165px">Photo Gallery</h3>
  <div class="grid" style="left:22px"><span role="img" aria-label="Farm photo"></span><span role="img" aria-label="Farm photo"></span><span role="img" aria-label="Farm photo"></span><span role="img" aria-label="Farm photo"></span><span role="img" aria-label="Farm photo"></span><span role="img" aria-label="Farm photo"></span></div>
  <h3 style="left:212px;top:162px;width:165px">Recent <span class="accent">Works</span></h3>
  <div class="grid" style="left:212px"><span role="img" aria-label="Project photo"></span><span role="img" aria-label="Project photo"></span><span role="img" aria-label="Project photo"></span><span role="img" aria-label="Project photo"></span><span role="img" aria-label="Project photo"></span><span role="img" aria-label="Project photo"></span></div>
  <h3 style="left:403px;top:162px;width:165px">Recent Tweet</h3>
  <div class="tweet">
    <svg class="abs" style="left:0;top:3px" width="18" height="14" viewBox="0 0 18 14"><path d="M1 4l8 4 8-4v9H1z" fill="#666"/></svg>
    Lorem ipsum dolor sit amet, sum dolor sitamet, con-sectetuer adipiscing elit, sed diam... <span class="accent">85 days ago</span>
  </div>
  <h3 style="left:592px;top:162px;width:165px">Useful <span class="accent">Links</span></h3>
  <div class="links"><span>About</span><span>Activities</span><span>Events</span><span>Members</span><span>Career</span><span>Contact</span></div>
</footer>
<div class="abs copyright">© Copyright FieldNorth. All rights reserved.</div>

</body>
</html>
```